Property inspection company needs logo/business card design

A new, home, commercial, and multi dwelling inspection company needs help with a new logo and hence business cards.

Time is extended for the rest of the week.

Font styles to use
Sans Serif

Colors
ec1f27
0255a3
ffffff

```html
<!DOCTYPE html>
<html lang="en">
<head>
<meta charset="utf-8">
<title>Ray Calloway Property Inspections – Business Card</title>
<link rel="stylesheet" href="https://fonts.googleapis.com/css2?family=Oswald:wght@600&family=Open+Sans:wght@400&display=swap">
<style>
  :root {
    --backdrop: #e9e6e3;
    --brand-red: #a91e25;
    --stripe-grey: #6d6e71;
    --card-light: #f4f3f3;
    --card-light-edge: #e6e5e5;
    --text-white: #ffffff;
  }
  * { margin: 0; padding: 0; box-sizing: border-box; }
  html, body {
    width: 1200px;
    height: 900px;
    overflow: hidden;
    background: var(--backdrop);
  }
  .business-card {
    position: absolute;
    left: 150px;
    top: 171px;
    width: 900px;
    height: 558px;
    overflow: hidden;
    box-shadow: 0 10px 30px rgba(0, 0, 0, 0.18);
  }
  .card-shapes {
    position: absolute;
    inset: 0;
  }
  .contact-panel {
    position: absolute;
    left: 52px;
    top: 132px;
    color: var(--text-white);
    font-family: "Open Sans", sans-serif;
  }
  .person-name {
    font-family: "Oswald", sans-serif;
    font-weight: 600;
    font-size: 41px;
    line-height: 1;
    letter-spacing: 0.2px;
  }
  .person-title {
    font-size: 25px;
    line-height: 1.2;
    margin-top: 2px;
  }
  .contact-list {
    list-style: none;
    margin-top: 24px;
  }
  .contact-list li {
    display: flex;
    align-items: center;
    font-size: 26px;
    line-height: 33px;
  }
  .contact-icon {
    width: 20px;
    height: 20px;
    margin-right: 12px;
    fill: var(--text-white);
    flex: none;
  }
  .address {
    font-size: 26px;
    line-height: 33px;
    margin-top: 18px;
  }
  .company-name {
    position: absolute;
    left: 520px;
    width: 360px;
    top: 232px;
    text-align: center;
    font-family: "Open Sans", sans-serif;
    font-weight: 400;
    font-size: 26px;
    line-height: 36px;
    color: var(--brand-red);
  }
</style>
</head>
<body>
  <div class="business-card">
    <svg class="card-shapes" width="900" height="558" viewBox="0 0 900 558" aria-hidden="true">
      <defs>
        <linearGradient id="lightSide" x1="0" y1="0" x2="1" y2="1">
          <stop offset="0" stop-color="var(--card-light-edge)"/>
          <stop offset="0.5" stop-color="var(--card-light)"/>
          <stop offset="1" stop-color="var(--card-light-edge)"/>
        </linearGradient>
      </defs>
      <rect width="900" height="558" fill="url(#lightSide)"/>
      <polygon class="stripe" points="310,0 322,0 590,558 578,558" fill="var(--stripe-grey)"/>
      <polygon class="red-panel" points="0,0 303,0 571,558 0,558" fill="var(--brand-red)"/>
    </svg>

    <div class="contact-panel">
      <h1 class="person-name">DANIEL HART</h1>
      <p class="person-title">Managing Director</p>
      <ul class="contact-list">
        <li>
          <svg class="contact-icon" viewBox="0 0 20 20" aria-hidden="true"><path d="M2 8c0-3 4-5 8-5s8 2 8 5l-3 1-1-2c-1-.5-3-.7-4-.7S7 6.5 6 7L5 9zM5 10h10l2 6H3z"/></svg>
          044-123 456 789
        </li>
        <li>
          <svg class="contact-icon" viewBox="0 0 20 20" aria-hidden="true"><path d="M6 1h8a1 1 0 0 1 1 1v16a1 1 0 0 1-1 1H6a1 1 0 0 1-1-1V2a1 1 0 0 1 1-1zm1 3v11h6V4zm3 12.5a1 1 0 1 0 0 .01z"/></svg>
          044-123 456 789
        </li>
        <li>
          <svg class="contact-icon" viewBox="0 0 20 20" aria-hidden="true"><path d="M2 5h16v10H2zm1.5 1.2V7l6.5 4 6.5-4v-.8z"/></svg>
          info@webname.com
        </li>
        <li>
          <svg class="contact-icon" viewBox="0 0 20 20" aria-hidden="true"><circle cx="10" cy="10" r="8"/></svg>
          www.websitename.com
        </li>
      </ul>
      <p class="address">12345, Address Goes Here<br>Country Name, 123456.</p>
    </div>

    <p class="company-name">Ray Calloway<br>Property Inspections Inc</p>
  </div>
</body>
</html>
```